Berrocal Tizón Law Firm for Small and Medium Business: Website

We need a web design that includes coding for the Wix platform, for a new company based in Santiago, Chile, called Berrocal Tizón, Abogados y Consultores. The company is essentially a law firm, with additional advisory services in accounting, tax management and finance. The main target of the company are founders, CEOs or C-level executives of small or medium companies based in Chile.
The main menu of the web page must have the following tab options:
- Home - About us - Services – How we work -Blog – FAQ -Contact
Our main services are:

1.- Commercial and corporate law advisory
2.- Legal defense in civil, criminal, labor and family matters (litigation and arbitration)
3.- Bankruptcy and reorganization of companies
4.- Collection and recovery of assets
5.- Asset protection
6.- Financial and tax advice

We want to highlight the following services:

-Bankruptcy and reorganization of companies
-Judicial defense in civil matters
-Financial and tax advice

In addition to these services, the following will be offered:
-Lawyer at your home for special cases
-Half hour free consultation
-Monthly service packages

The final design should communicate confidence, business savvy and high execution standards and quality.

Target Market(s)

The main target of the company are founders, CEOs or C-level executives of small or medium companies based in Chile.

Industry/Entity Type

Legal industry

Coding

Number of Pages Required

5+ page

Font styles to use
Serif

Requirements
Must have
• 1. Big banners para destacar los siguientes servicios: -Bankruptcy and reorganization of companies -Judicial defense in civil matters -Financial and tax advice 2. Call to action para agendar consulta legal. 3. Destacar los siguientes servicios: -Lawyer at your home for special cases -Half hour free consultation -Monthly service packages 3. Página para explicar cómo se cobra (precios transparentes): ver el siguiente sitio web: https://www.brookvanelegal.example/how 4. Links to Facebook, Instagram and Linkedin 5. Connection to Whatsapp.
Should not have
• Look old fashioned

```html
<!DOCTYPE html>
<html lang="en">
<head>
<meta charset="utf-8">
<title>Berrocal Tizón — Abogados y Consultores</title>
<link href="https://fonts.googleapis.com/css2?family=Brawler:wght@400;700&family=Rubik:wght@400&display=swap" rel="stylesheet">
<style>
:root{
  --dark:#1b2f2a;
  --teal:#3b6559;
  --gold:#bdae4e;
  --accent:#e8dc6a;
  --paper:#f3f3f3;
  --white:#ffffff;
  --ink:#1c1c1c;
  --serif:'Brawler', Georgia, serif;
  --sans:'Rubik', Arial, sans-serif;
}
*{margin:0;padding:0;box-sizing:border-box}
html,body{width:1200px;height:2769px;overflow:hidden}
body{position:relative;background:var(--white);font-family:var(--serif);color:var(--ink)}
.abs{position:absolute}

/* navigation */
.topbar{left:0;top:0;width:1200px;height:83px;background:var(--dark)}
.brand{display:flex;align-items:center;gap:8px;color:var(--gold);font-family:var(--serif)}
.brand-mark{width:38px;height:38px;border:2px solid var(--gold)}
.brand-name{font-size:26px;line-height:1}
.brand-sub{font-size:8px;letter-spacing:1.5px;margin-top:3px}
.topbar .brand{position:absolute;left:116px;top:22px}
.menu{position:absolute;left:441px;top:30px;display:flex;gap:32px;font-size:16px;color:var(--white)}
.contact-btn{position:absolute;left:975px;top:23px;width:108px;height:37px;border:1px solid var(--white);color:var(--white);font-size:16px;display:flex;align-items:center;justify-content:center;gap:8px}

/* hero */
.hero-photo{left:0;top:83px;width:1200px;height:501px;background:linear-gradient(120deg,#4d6f68 0%,#86a29a 45%,#5f7d76 70%,#7d958f 100%)}
.hero-panel{left:116px;top:83px;width:422px;height:501px;background:var(--dark)}
.hero-title{position:absolute;left:0;top:40px;width:422px;text-align:center;font-size:47px;line-height:50px;color:var(--white)}
.hero-services{position:absolute;left:0;top:286px;width:422px;height:132px;background:var(--teal);display:flex}
.hero-service{flex:1;display:flex;flex-direction:column;align-items:center;padding-top:14px;text-align:center;font-size:12px;line-height:18px;color:var(--white);border-right:1px solid rgba(255,255,255,.35);margin:16px 0 14px;padding-left:10px;padding-right:10px}
.hero-service{margin-top:0;padding-top:14px}
.hero-service:last-child{border-right:none}
.hero-service svg{margin-bottom:14px}
.hero-cta{position:absolute;left:0;top:418px;width:422px;height:33px;background:var(--gold);color:var(--white);font-size:14px;display:flex;align-items:center;justify-content:center;gap:12px}

/* about */
.about{left:0;top:584px;width:1200px;height:668px;background:var(--paper)}
.about-backing{left:0;top:163px;width:508px;height:333px;background:var(--dark)}
.about-photo{left:21px;top:143px;width:509px;height:334px;background:linear-gradient(135deg,#3a2d24 0%,#4a3a2e 40%,#5a5550 70%,#2c2520 100%)}
.eyebrow{font-size:18px;display:inline-block;position:relative;padding-bottom:6px}
.eyebrow::after{content:"";position:absolute;left:0;bottom:0;width:108px;height:4px;background:var(--accent)}
.about .eyebrow{position:absolute;left:587px;top:72px}
.about-title{position:absolute;left:587px;top:104px;width:520px;font-size:34px;line-height:42px;font-weight:400}
.about-copy{position:absolute;left:587px;top:198px;width:500px;font-family:var(--sans);font-size:15.6px;line-height:28.3px;color:#222}

/* offers */
.offers-head{left:0;top:1324px;width:1200px;text-align:center}
.offers-head .eyebrow{font-size:18px}
.offers-head .eyebrow::after{left:18px}
.offers-title{font-size:34px;font-weight:400;margin-top:10px}
.offers{left:116px;top:1432px;width:967px;height:268px;background:var(--dark);display:flex}
.offer{flex:1;display:flex;flex-direction:column;align-items:center;margin:15px 0;border-right:1px solid rgba(255,255,255,.25)}
.offer:last-child{border-right:none}
.offer-icon{width:107px;height:107px;border:3px solid var(--accent);border-radius:50%;margin-top:18px;display:flex;align-items:center;justify-content:center}
.offer-label{margin-top:28px;text-align:center;font-size:20px;line-height:32px;letter-spacing:1px;color:var(--white)}

/* consultation */
.consult{left:0;top:1774px;width:1200px;height:623px;background:linear-gradient(100deg,#3d4f4a 0%,#5b6f69 35%,#4a5c57 60%,#6a7e78 100%)}
.consult-title{position:absolute;left:116px;top:78px;font-size:47px;line-height:50px;font-weight:700;color:var(--white)}
.consult-copy{position:absolute;left:116px;top:198px;width:320px;font-family:var(--sans);font-size:17.5px;line-height:27px;color:var(--white)}
.form-panel{position:absolute;left:587px;top:75px;width:496px;height:475px;background:var(--dark)}
.field{position:absolute;background:var(--white);font-family:var(--sans);font-size:15px;color:#aaa;padding:18px 17px}
.submit{position:absolute;left:26px;top:395px;width:445px;height:54px;background:var(--gold);color:var(--white);font-size:18px;display:flex;align-items:center;justify-content:center}

/* footer */
.footer{left:0;top:2397px;width:1200px;height:372px;background:var(--dark);color:var(--white);text-align:center}
.footer .brand{position:absolute;left:476px;top:80px}
.footer-tagline{position:absolute;left:0;top:144px;width:1200px;font-size:20px;line-height:23px;font-weight:700}
.footer-menu{position:absolute;left:0;top:218px;width:1200px;display:flex;justify-content:center;gap:34px;font-size:16px}
.social{position:absolute;left:0;top:265px;width:1200px;display:flex;justify-content:center;gap:38px}
.social span{width:32px;height:32px;border:2px solid var(--white);border-radius:6px;display:block}
</style>
</head>
<body>

<header class="abs topbar">
  <div class="brand">
    <span class="brand-mark"></span>
    <div><div class="brand-name">Berrocal Tizón</div><div class="brand-sub">ABOGADOS Y CONSULTORES</div></div>
  </div>
  <nav class="menu"><span>Home</span><span>About Us</span><span>Services</span><span>How We Work</span><span>Blog</span><span>FAQ</span></nav>
  <div class="contact-btn">Contact
    <svg width="16" height="16" viewBox="0 0 24 24" fill="#fff"><path d="M6.6 10.8a15 15 0 0 0 6.6 6.6l2.2-2.2a1 1 0 0 1 1-.25 11.4 11.4 0 0 0 3.6.6 1 1 0 0 1 1 1V20a1 1 0 0 1-1 1A17 17 0 0 1 3 4a1 1 0 0 1 1-1h3.5a1 1 0 0 1 1 1c0 1.25.2 2.45.6 3.6a1 1 0 0 1-.25 1z"/></svg>
  </div>
</header>

<section>
  <div class="abs hero-photo" role="img" aria-label="Confident lawyer in a dark suit with arms crossed before glass office towers, green-tinted"></div>
  <div class="abs hero-panel">
    <h1 class="hero-title" style="font-weight:400">Protecting Assets &amp; Preserving Futures with A Plan of Actions</h1>
    <div class="hero-services">
      <div class="hero-service">
        <svg width="34" height="34" viewBox="0 0 34 34" fill="none" stroke="#fff" stroke-width="1.5"><rect x="4" y="4" width="20" height="26"/><path d="M8 10h12M8 15h12M8 20h8"/><path d="M22 22l8 8"/></svg>
        Bankruptcy and reorganization of companies</div>
      <div class="hero-service">
        <svg width="34" height="34" viewBox="0 0 34 34" fill="none" stroke="#fff" stroke-width="1.5"><path d="M17 4v24M8 30h18M6 9h22M6 9l-4 9h8zM28 9l-4 9h8z"/></svg>
        Judicial defense in civil matters</div>
      <div class="hero-service">
        <svg width="34" height="34" viewBox="0 0 34 34" fill="none" stroke="#fff" stroke-width="1.5"><rect x="6" y="3" width="22" height="28"/><path d="M10 10h14M10 15h14M10 20h6"/><circle cx="22" cy="24" r="4"/></svg>
        Financial and tax advice</div>
    </div>
    <div class="hero-cta">Schedule Legal Consultation
      <svg width="8" height="12" viewBox="0 0 8 12" fill="none" stroke="#fff" stroke-width="1.5"><path d="M1 1l5 5-5 5"/></svg>
    </div>
  </div>
</section>

<section class="abs about">
  <div class="abs about-backing"></div>
  <div class="abs about-photo" role="img" aria-label="Team of six lawyers posing in a wood-panelled office with bookshelves"></div>
  <span class="eyebrow">About Us</span>
  <h2 class="about-title">You Know Like No Other How It Feels To Be On The Edge</h2>
  <p class="about-copy">Nobody has given you anything, but it is because you know how to take risks in a calculated way. However, you feel when there is a danger, you know how to react in time to it. In this new era, you know that you must be alert to the signs of a constantly surprising and disruptive environment that can destroy everything you built: Your Wealth and Assets. Berrocal Tizón, Abogados y Consultores is here to shield your business and protect what with so much work and effort you have created. Your business, your life and your family are much more connected than you think. And many times, they are interdependant. A bad business, which can always happen, can effect your personal or family assets, and you need to be well advised and protected. And that is why we have an offer specially designed for you and your company.</p>
</section>

<section>
  <div class="abs offers-head">
    <span class="eyebrow">Why Choose Us?</span>
    <h2 class="offers-title">Special Service We Provide</h2>
  </div>
  <div class="abs offers">
    <div class="offer">
      <div class="offer-icon"><svg width="56" height="56" viewBox="0 0 56 56" fill="none" stroke="#e8dc6a" stroke-width="3"><circle cx="28" cy="17" r="9"/><path d="M12 48V38a8 8 0 0 1 8-8h16a8 8 0 0 1 8 8v10zM28 30v18"/></svg></div>
      <div class="offer-label">Lawyer at your home for<br>special cases</div>
    </div>
    <div class="offer">
      <div class="offer-icon"><svg width="60" height="60" viewBox="0 0 60 60" fill="none" stroke="#e8dc6a" stroke-width="4"><circle cx="30" cy="30" r="24"/><path d="M28 16v16h12"/></svg></div>
      <div class="offer-label">Half hour free<br>consultation</div>
    </div>
    <div class="offer">
      <div class="offer-icon"><svg width="56" height="56" viewBox="0 0 56 56" fill="none" stroke="#e8dc6a" stroke-width="3"><circle cx="30" cy="12" r="5"/><path d="M22 28a8 8 0 0 1 16 0zM8 36l10-4h12a3 3 0 0 1 0 6h-8M30 38l14-6a3 3 0 0 1 3 5L32 46H14l-6 2"/></svg></div>
      <div class="offer-label">Monthly service<br>packages</div>
    </div>
  </div>
</section>

<section class="abs consult" role="img" aria-label="Historic courtroom with wooden benches, green-tinted">
  <h2 class="consult-title">Get Your Free<br>Consultation Now</h2>
  <p class="consult-copy">Fill the form to get half hour of free consultation with our best lawyer</p>
  <div class="form-panel">
    <div class="field" style="left:26px;top:26px;width:209px;height:54px">First Name</div>
    <div class="field" style="left:262px;top:26px;width:209px;height:54px">Last Name</div>
    <div class="field" style="left:26px;top:105px;width:445px;height:54px">Email</div>
    <div class="field" style="left:26px;top:185px;width:445px;height:54px">Phone Number</div>
    <div class="field" style="left:26px;top:264px;width:445px;height:105px">Message</div>
    <div class="submit">Get Free Consultation</div>
  </div>
</section>

<footer class="abs footer">
  <div class="brand">
    <span class="brand-mark"></span>
    <div style="text-align:left"><div class="brand-name">Berrocal Tizón</div><div class="brand-sub">ABOGADOS Y CONSULTORES</div></div>
  </div>
  <p class="footer-tagline">Protecting Assets &amp; Preserving Futures with A<br>Plan of Actions</p>
  <nav class="footer-menu"><span>Home</span><span>About Us</span><span>Services</span><span>How We Work</span><span>Blog</span><span>FAQ</span><span>Contact</span></nav>
  <div class="social">
    <span role="img" aria-label="Messaging link"></span>
    <span role="img" aria-label="Photo network link"></span>
    <span role="img" aria-label="Social network link"></span>
    <span role="img" aria-label="Professional network link"></span>
  </div>
</footer>

</body>
</html>
```